Real Estate Investing company needs a business card design

We need a business card design for new Real Estate Investment Company called "Maple Ridge Ventures, LLC." We buy homes for cash and close quickly in any situation. Our company provides an easy and fast option for home owners who are in tough situations who need to sell their home fast and don't want realtor fees or other listing hassles. We also renovate and resell our homes which helps provide housing for the community. We would like to see designs that use the colors blue and white to match our company logo or other colors that may match our company logo. The final design should communicate trust and easy process.
Industry/Entity Type
Business
Contact Information for Business Card
Front should have company name and company logo. back of card should have company logo and area to list services.
Look and feel

```html
<!DOCTYPE html>
<html lang="en">
<head>
<meta charset="utf-8">
<title>Maple Ridge Ventures – Business Cards</title>
<link rel="stylesheet" href="https://fonts.googleapis.com/css2?family=Open+Sans:wght@400;600;700&display=swap">
<style>
  :root {
    --backdrop: #3a302c;
    --card-dark: #151515;
    --card-dark-mark: #2c2c2c;
    --card-light: #f7f7f5;
    --brand-blue: #1f6bb6;
    --divider: #dcdcdc;
  }
  * { margin: 0; padding: 0; box-sizing: border-box; }
  html, body { width: 1200px; height: 716px; overflow: hidden; }
  body {
    background: var(--backdrop);
    font-family: "Open Sans", Arial, sans-serif;
    position: relative;
  }
  .card {
    position: absolute;
    top: 210px;
    width: 520px;
    height: 297px;
    border-radius: 3px;
    box-shadow: 0 12px 28px rgba(0,0,0,0.45);
    overflow: hidden;
  }
  .card--front {
    left: 50px;
    background: var(--card-dark);
    display: flex;
    align-items: center;
    justify-content: center;
  }
  .card--back {
    left: 630px;
    background: var(--card-light);
    display: flex;
  }
  .brand-name {
    font-weight: 700;
    text-transform: uppercase;
    line-height: 1.05;
    text-align: center;
    letter-spacing: 0.02em;
  }
  .card--front .brand-name {
    color: var(--card-dark-mark);
    font-size: 40px;
  }
  .card__brand-side {
    width: 46%;
    display: flex;
    align-items: center;
    justify-content: center;
    gap: 10px;
    border-right: 1px solid var(--divider);
    margin: 40px 0;
    padding: 0 14px;
  }
  .brand-square {
    width: 14px; height: 14px;
    background: var(--brand-blue);
    flex: none;
  }
  .card--back .brand-name {
    color: var(--brand-blue);
    font-size: 24px;
    text-align: left;
  }
  .card__contact-side {
    flex: 1;
    min-width: 0;
    padding: 74px 18px 0 22px;
    color: var(--brand-blue);
  }
  .contact__name {
    font-size: 21px;
    font-weight: 700;
    line-height: 1.1;
  }
  .contact__title {
    font-size: 10px;
    margin-bottom: 14px;
  }
  .contact__line {
    display: flex;
    align-items: center;
    gap: 9px;
    font-size: 11.5px;
    line-height: 1.55;
    white-space: nowrap;
  }
  .contact__line svg { width: 11px; height: 11px; fill: var(--brand-blue); flex: none; }
  .contact__address {
    font-size: 11.5px;
    line-height: 1.45;
    margin-top: 2px;
  }
</style>
</head>
<body>
  <section class="card card--front" aria-label="Card front">
    <div class="brand-name">Maple Ridge<br>Ventures</div>
  </section>

  <section class="card card--back" aria-label="Card back">
    <div class="card__brand-side">
      <span class="brand-square"></span>
      <div class="brand-name">Maple Ridge<br>Ventures</div>
    </div>
    <div class="card__contact-side">
      <div class="contact__name">YOUR NAME</div>
      <div class="contact__title">Managing Director</div>
      <div class="contact__line">
        <svg viewBox="0 0 12 12" aria-hidden="true"><path d="M2 1h2.5l1 3-1.5 1a6 6 0 0 0 3 3l1-1.5 3 1V10a1 1 0 0 1-1 1A9 9 0 0 1 1 2a1 1 0 0 1 1-1z"/></svg>
        <span>+00 111 222 3333</span>
      </div>
      <div class="contact__line">
        <svg viewBox="0 0 12 12" aria-hidden="true"><path d="M1 3h10v7H1z M1 3l5 4 5-4" fill="none" stroke="#1f6bb6" stroke-width="1.3"/></svg>
        <span>yourname@mapleridgeventures.com</span>
      </div>
      <div class="contact__address">Your Long Commercial or<br>business address in 2 line</div>
    </div>
  </section>
</body>
</html>
```